Home Improvements Website

I would like a website that matches our business colour scheme and uses the fonts consistent without logo. (Monserrat, Chosence & Big Noddle Tiling).
We will need numerous sections: homepage, about us, services (with tiles or links to each service - building, landscaping, decking, maintenance, roofing, gutters etc) current projects (which must be easily editable by me, who is not too tech savvy) and a contacts page with enquiry form we can link to our job management service (Tradify).

```html
<!DOCTYPE html>
<html lang="en">
<head>
<meta charset="utf-8">
<title>Verdant Ridge — Home Improvements</title>
<link rel="stylesheet" href="https://fonts.googleapis.com/css2?family=Rubik:wght@300;400;500;600;700;800&display=swap">
<style>
:root{
  --green:#56bb2c;
  --green-bright:#4fb52a;
  --green-dark:#14912c;
  --green-soft:#9fd57c;
  --tan:#b9853f;
  --ink:#1d1d1d;
  --text:#333;
  --grey-band:#ececec;
  --footer:#242424;
  --footer-card:#1c1c1c;
  --white:#fff;
}
*{margin:0;padding:0;box-sizing:border-box}
html,body{width:1200px;height:4622px;overflow:hidden}
body{position:relative;font-family:"Rubik",sans-serif;color:var(--text);background:var(--white)}
.abs{position:absolute}
a{color:inherit;text-decoration:none}

/* header */
.topbar-phone{left:640px;top:0;width:203px;height:33px;background:var(--green-dark);color:#fff;font-size:14px;display:flex;align-items:center;justify-content:center;gap:6px}
.topbar-mail{left:843px;top:0;width:230px;height:33px;background:var(--tan);color:#fff;font-size:14px;display:flex;align-items:center;justify-content:center;gap:6px;clip-path:polygon(0 0,100% 0,94% 100%,0 100%)}
.brand{left:128px;top:18px;display:flex;align-items:center;gap:8px;z-index:3}
.brand-square{width:22px;height:22px;background:var(--green-dark)}
.brand-name{font-size:19px;font-weight:700;line-height:1.05;color:var(--ink);text-transform:uppercase}
.nav{left:414px;top:56px;display:flex;gap:0;font-size:15px;color:var(--ink)}
.nav a{position:absolute;white-space:nowrap}
.nav .active{color:var(--green-dark)}
.quote-btn{left:884px;top:48px;width:185px;height:38px;border-radius:19px;background:var(--green-dark);color:#fff;font-size:15px;font-weight:500;display:flex;align-items:center;justify-content:center;gap:8px}

/* hero */
.hero{left:0;top:99px;width:1200px;height:710px;background:linear-gradient(180deg,#6b7470 0%,#4f5f4a 30%,#3f6b2a 55%,#3f8a27 78%,#5aa534 100%)}
.hero-house{left:700px;top:99px;width:500px;height:540px;background:linear-gradient(160deg,#aab6c6 0%,#8593a6 45%,#4d6b3c 100%);opacity:.85}
.hero-cut{left:0;top:640px}
.hero-kicker{left:131px;top:248px;color:#fff;font-size:23px;font-weight:500;line-height:32px;width:420px}
.hero-title{left:131px;top:318px;color:#fff;font-size:46px;font-weight:600;line-height:52px;width:480px}
.hero-btn{left:135px;top:508px;width:188px;height:50px;background:var(--tan);border-radius:3px;color:#fff;font-size:16px;font-weight:600;display:flex;align-items:center;justify-content:center;gap:8px;text-transform:uppercase}

/* about */
.mark-square{width:44px;height:44px;background:var(--green)}
.about-mark{left:150px;top:886px}
.about-title{left:135px;top:948px;font-size:46px;font-weight:700;color:var(--ink);letter-spacing:-.5px}
.about-title span{color:var(--green)}
.about-text{left:135px;top:1014px;width:450px;font-size:17px;line-height:29px;color:#333}
.about-hex-outer{left:687px;top:838px;width:382px;height:440px;background:var(--green);clip-path:polygon(50% 0,100% 25%,100% 75%,50% 100%,0 75%,0 25%)}
.about-hex-mid{left:701px;top:854px;width:354px;height:408px;background:#fff;clip-path:polygon(50% 0,100% 25%,100% 75%,50% 100%,0 75%,0 25%)}
.about-hex-img{left:709px;top:864px;width:338px;height:388px;clip-path:polygon(50% 0,100% 25%,100% 75%,50% 100%,0 75%,0 25%);background:linear-gradient(180deg,#6b4a35 0%,#7a5a3e 30%,#4e8f3a 55%,#5fae37 100%)}

/* services */
.services-bg{left:0;top:1300px}
.services-title{left:0;top:1440px;width:1200px;text-align:center;color:#fff;font-size:43px;font-weight:400}
.tile{width:233px;height:262px;clip-path:polygon(50% 0,100% 25%,100% 75%,50% 100%,0 75%,0 25%);background:var(--green-soft)}
.tile-inner{position:absolute;left:6px;top:7px;width:221px;height:248px;clip-path:polygon(50% 0,100% 25%,100% 75%,50% 100%,0 75%,0 25%)}
.tile-label{position:absolute;left:0;top:176px;width:233px;text-align:center;color:#fff;font-size:19px;font-weight:600;text-transform:uppercase}
.tone-deck{background:linear-gradient(180deg,#2b3440 0%,#6b6560 45%,#b9aa98 100%)}
.tone-roof{background:linear-gradient(160deg,#5d6b7d 0%,#c98a3c 45%,#6f6c6a 100%)}
.tone-land{background:linear-gradient(180deg,#e6ecef 0%,#7fb148 45%,#3f8a2b 100%)}
.tone-maint{background:linear-gradient(180deg,#dfe6ec 0%,#8d949b 45%,#4c7b35 100%)}
.tone-gutter{background:linear-gradient(160deg,#8a3b2c 0%,#b56a55 50%,#4a8a33 100%)}

/* why */
.why-title{left:0;top:2236px;width:1200px;text-align:center;font-size:43px;font-weight:700;color:var(--ink)}
.why-rule{left:565px;top:2294px;width:70px;height:3px;background:var(--green)}
.why-text{left:0;top:2313px;width:1200px;text-align:center;font-size:18px;line-height:30px;color:#222}
.why-item{width:240px;text-align:center}
.why-item svg{display:block;margin:0 auto}
.why-label{margin-top:18px;font-size:22px;color:#222}

/* latest work */
.work-mark{left:578px;top:2640px}
.work-title{left:0;top:2728px;width:1200px;text-align:center;font-size:46px;font-weight:700;color:var(--ink)}
.work-title span{color:var(--green)}
.work-img{position:absolute}
.w1{left:136px;top:2827px;width:456px;height:269px;background:linear-gradient(160deg,#8a5b45 0%,#6fae3f 45%,#5e6670 100%)}
.w2{left:601px;top:2827px;width:459px;height:269px;background:linear-gradient(180deg,#dfe3e6 0%,#9a8a80 50%,#7d706a 100%)}
.w3{left:136px;top:3105px;width:302px;height:270px;background:linear-gradient(180deg,#6b4e33 0%,#7a5a3b 40%,#5aa838 65%,#a87a4e 100%)}
.w4{left:447px;top:3105px;width:301px;height:270px;background:linear-gradient(180deg,#2f9a3f 0%,#23903a 100%)}
.w5{left:757px;top:3105px;width:301px;height:270px;background:linear-gradient(180deg,#c5d2da 0%,#9c7344 45%,#4e9a34 100%)}
.view-more{left:447px;top:3105px;width:301px;height:270px;color:#fff;text-align:center}
.view-more .ring{position:absolute;left:132px;top:97px;width:36px;height:36px;border-radius:50%;background:#fff;display:flex;align-items:center;justify-content:center}
.view-more .label{position:absolute;left:0;top:152px;width:301px;font-size:27px;font-weight:500}
.learn-btn{left:504px;top:3414px;width:188px;height:48px;background:var(--green);color:#fff;font-size:16px;font-weight:500;display:flex;align-items:center;justify-content:center;gap:8px;border-radius:2px}

/* testimonial */
.testi-band{left:0;top:3520px;width:1200px;height:301px;background:var(--grey-band)}
.arrow-btn{width:40px;height:40px;border-radius:50%;display:flex;align-items:center;justify-content:center}
.arrow-prev{left:199px;top:3645px;border:2px solid var(--green-soft)}
.arrow-next{left:961px;top:3645px;background:var(--green)}
.testi-photo{left:310px;top:3620px;width:101px;height:101px;background:linear-gradient(160deg,#f1e6da 0%,#d9b89a 60%,#b08a6a 100%);border-radius:3px}
.testi-badge{left:397px;top:3706px;width:20px;height:20px;background:var(--green);border:2px solid #fff}
.testi-quote{left:432px;top:3624px;width:450px;font-size:14px;line-height:21px;color:#333}
.testi-meta{left:432px;top:3702px;font-size:14px;font-weight:600;color:var(--green);letter-spacing:.5px;display:flex;gap:14px;align-items:center}
.testi-meta .sep{color:#444;font-weight:400}
.stars{color:#e1582a;letter-spacing:2px}

/* call to action */
.cta-photo{left:0;top:3821px;width:1200px;height:450px;background:linear-gradient(180deg,#3d4a42 0%,#3f5a38 35%,#2f6e24 65%,#3e8a2a 100%)}
.cta-shade{left:0;top:3821px;width:1200px;height:450px;background:rgba(0,0,0,.28)}
.cta-title{left:0;top:3924px;width:1200px;text-align:center;color:#fff;font-size:31px;font-weight:700;line-height:46px;letter-spacing:-1px;text-transform:uppercase}
.cta-btn{left:479px;top:4038px;width:242px;height:45px;background:var(--green);color:#fff;font-size:16px;font-weight:500;display:flex;align-items:center;justify-content:center;gap:8px;text-transform:uppercase}

/* footer */
.footer-shape{left:0;top:4140px}
.estimate-card{left:775px;top:4140px;width:294px;height:359px;background:var(--footer-card);box-shadow:0 6px 18px rgba(0,0,0,.45);color:#fff}
.estimate-card h3{position:absolute;left:0;top:24px;width:294px;text-align:center;font-size:16px;font-weight:600;text-transform:uppercase}
.estimate-card p{position:absolute;left:40px;top:46px;width:214px;text-align:center;font-size:9px;line-height:11px;color:#ddd}
.field{position:absolute;height:21px;border:1px solid #555;font-size:8px;color:#eee;padding:5px 8px;text-transform:uppercase;font-weight:500}
.field-select-btn{position:absolute;right:0;top:0;width:26px;height:19px;background:var(--green);display:flex;align-items:center;justify-content:center}
.card-btn{position:absolute;left:122px;top:273px;width:156px;height:25px;background:var(--green);font-size:9px;font-weight:600;display:flex;align-items:center;justify-content:center;gap:6px;text-transform:uppercase}
.footer-brand{left:190px;top:4370px;display:flex;align-items:center;gap:8px}
.footer-brand .brand-name{color:#fff;font-size:20px}
.footer-brand .brand-square{background:var(--green)}
.fcol{font-size:13px;color:#fff;text-transform:uppercase;font-weight:500}
.flink{position:absolute;white-space:nowrap}
.fsub{font-size:12px;text-transform:none;text-decoration:underline;font-weight:400}
.social{left:524px;top:4500px;display:flex;gap:8px}
.social span{width:33px;height:33px;border-radius:50%;border:1.5px solid #bbb;display:block}
.footer-rule{left:0;top:4557px;width:1200px;height:1px;background:#444}
.copyright{left:0;top:4578px;width:1200px;text-align:center;font-size:14px;color:#ccc}
</style>
</head>
<body>

<!-- header -->
<div class="abs topbar-phone">
  <svg width="12" height="12" viewBox="0 0 24 24" fill="#fff"><path d="M6.6 10.8a15 15 0 0 0 6.6 6.6l2.2-2.2c.3-.3.7-.4 1-.2 1.1.4 2.3.6 3.6.6.6 0 1 .4 1 1V20c0 .6-.4 1-1 1A17 17 0 0 1 3 4c0-.6.4-1 1-1h3.5c.6 0 1 .4 1 1 0 1.3.2 2.5.6 3.6.1.3 0 .7-.2 1z"/></svg>
  +1 555 014 2290
</div>
<div class="abs topbar-mail">
  <svg width="13" height="10" viewBox="0 0 24 18" fill="#fff"><path d="M0 0h24v18H0z" fill="none"/><path d="M1 1h22v16H1z" fill="#fff"/><path d="M1 1l11 9 11-9" stroke="#b9853f" stroke-width="2" fill="none"/></svg>
  info@verdantridge.com
</div>

<div class="abs brand">
  <span class="brand-square"></span>
  <span class="brand-name">Verdant<br>Ridge</span>
</div>

<nav class="abs nav">
  <a class="active" style="left:0;top:0">Home</a>
  <a style="left:78px;top:0">About Us</a>
  <a style="left:180px;top:0">Services</a>
  <a style="left:277px;top:0">Projects</a>
  <a style="left:374px;top:0">Contact</a>
</nav>
<a class="abs quote-btn">
  <svg width="16" height="16" viewBox="0 0 24 24" fill="none" stroke="#fff" stroke-width="2.2"><path d="M4 6h7M4 6v14h14v-7"/><path d="M17 3l4 4-9 9H8v-4z"/></svg>
  Request Quote
</a>

<!-- hero -->
<div class="abs hero" role="img" aria-label="Photo of a house with a curved stone path through a green lawn and flower beds"></div>
<div class="abs hero-house" role="img" aria-label="House facade and garden borders"></div>
<svg class="abs hero-cut" width="1200" height="170" viewBox="0 0 1200 170">
  <polygon points="0,24 600,167 1200,24 1200,170 0,170" fill="#fff"/>
</svg>
<div class="abs hero-kicker">we have a wealth of<br>knowledge and experience in the</div>
<h1 class="abs hero-title">Landscaping and Construction Industries</h1>
<a class="abs hero-btn">Get Started
  <svg width="16" height="16" viewBox="0 0 24 24"><circle cx="12" cy="12" r="11" fill="#fff"/><path d="M10 7l5 5-5 5" stroke="#b9853f" stroke-width="2.5" fill="none"/></svg>
</a>

<!-- about -->
<div class="abs mark-square about-mark"></div>
<h2 class="abs about-title">ABOUT <span>VERDANT</span></h2>
<p class="abs about-text">Lorem Ipsum is simply dummy text of the printing and typesetting industry. Lorem Ipsum has been the industry's standard dummy text ever since the 1500s, when an unknown printer took a galley of type and scrambled it to make a type specimen book. It has survived not only five</p>
<div class="abs about-hex-outer"></div>
<div class="abs about-hex-mid"></div>
<div class="abs about-hex-img" role="img" aria-label="Photo of a garden with a timber fence, shrubs and stepping stones across a lawn"></div>

<!-- services -->
<svg class="abs services-bg" width="1200" height="860" viewBox="0 0 1200 860">
  <polygon points="0,120 600,24 1200,120 1200,132 600,36 0,132" fill="var(--green-dark)"/>
  <polygon points="0,132 600,36 1200,132 1200,853 0,853" fill="var(--green)"/>
</svg>
<h2 class="abs services-title">OUR SERVICES</h2>

<div class="abs tile" style="left:160px;top:1546px"><div class="tile-inner tone-deck" role="img" aria-label="Photo of a timber deck with outdoor furniture"></div><div class="tile-label">Decking</div></div>
<div class="abs tile" style="left:419px;top:1546px"><div class="tile-inner tone-roof" role="img" aria-label="Photo of a roofer laying tiles"></div><div class="tile-label">Roofing</div></div>
<div class="abs tile" style="left:677px;top:1546px"><div class="tile-inner tone-land" role="img" aria-label="Photo of landscaped shrubs and lawn"></div><div class="tile-label">Landscaping</div></div>
<div class="abs tile" style="left:289px;top:1771px"><div class="tile-inner tone-maint" role="img" aria-label="Photo of a maintained house exterior"></div><div class="tile-label">Maintenance</div></div>
<div class="abs tile" style="left:546px;top:1771px"><div class="tile-inner tone-gutter" role="img" aria-label="Photo of a roof edge with gutters"></div><div class="tile-label">Gutters</div></div>
<div class="abs tile" style="left:806px;top:1771px"><div class="tile-inner tone-roof" role="img" aria-label="Photo of a roofer at work"></div><div class="tile-label">Roofing</div></div>

<!-- why choose us -->
<h2 class="abs why-title">WHY CHOOSE US?</h2>
<div class="abs why-rule"></div>
<p class="abs why-text">We understand how important your home is to you and work with you<br>to ensure you get the results you want.</p>

<div class="abs why-item" style="left:192px;top:2398px">
  <svg width="96" height="108" viewBox="0 0 96 108">
    <polygon points="48,3 92,28 92,80 48,105 4,80 4,28" fill="none" stroke="#9a9a9a" stroke-width="2.5"/>
    <circle cx="56" cy="44" r="12" fill="none" stroke="var(--green)" stroke-width="5"/>
    <path d="M47 53L30 70" stroke="var(--green)" stroke-width="6" stroke-linecap="round"/>
  </svg>
  <div class="why-label">Professionalism</div>
</div>
<div class="abs why-item" style="left:486px;top:2398px">
  <svg width="96" height="108" viewBox="0 0 96 108">
    <polygon points="48,3 92,28 92,80 48,105 4,80 4,28" fill="none" stroke="#9a9a9a" stroke-width="2.5"/>
    <circle cx="48" cy="54" r="22" fill="var(--green)"/>
    <path d="M37 54l8 8 15-16" stroke="#fff" stroke-width="5" fill="none" stroke-linecap="round"/>
  </svg>
  <div class="why-label">Better Results</div>
</div>
<div class="abs why-item" style="left:768px;top:2398px">
  <svg width="96" height="108" viewBox="0 0 96 108">
    <polygon points="48,3 92,28 92,80 48,105 4,80 4,28" fill="none" stroke="#9a9a9a" stroke-width="2.5"/>
    <path d="M32 40h28a7 7 0 0 1 0 14H36a7 7 0 0 0 0 14h28" fill="none" stroke="var(--green)" stroke-width="3.5" stroke-dasharray="5 4"/>
    <circle cx="32" cy="40" r="5" fill="var(--green)"/>
    <circle cx="64" cy="68" r="5" fill="var(--green)"/>
  </svg>
  <div class="why-label">Quality Work</div>
</div>

<!-- latest work -->
<div class="abs mark-square work-mark"></div>
<h2 class="abs work-title">LATEST <span>WORK</span></h2>
<div class="work-img w1" role="img" aria-label="Project photo: new lawn with paving and timber edging beside a brick wall"></div>
<div class="work-img w2" role="img" aria-label="Project photo: block paved driveway in front of a house"></div>
<div class="work-img w3" role="img" aria-label="Project photo: raised lawn with timber steps and a fence"></div>
<div class="work-img w4" role="img" aria-label="Project photo tinted green behind the view more link"></div>
<div class="abs view-more">
  <div class="ring"><svg width="14" height="14" viewBox="0 0 24 24" fill="none" stroke="#555" stroke-width="2.2"><path d="M14 4h6v6M20 4l-9 9M18 14v6H4V6h6"/></svg></div>
  <div class="label">View More</div>
</div>
<div class="work-img w5" role="img" aria-label="Project photo: new timber fence beside a lawn"></div>
<a class="abs learn-btn">LEARN MORE
  <svg width="16" height="16" viewBox="0 0 24 24"><circle cx="12" cy="12" r="11" fill="#fff"/><path d="M10 7l5 5-5 5" stroke="var(--green)" stroke-width="2.5" fill="none"/></svg>
</a>

<!-- testimonial -->
<div class="abs testi-band"></div>
<div class="abs arrow-btn arrow-prev"><svg width="14" height="14" viewBox="0 0 24 24"><path d="M15 5l-7 7 7 7" stroke="var(--green-soft)" stroke-width="3" fill="none"/></svg></div>
<div class="abs arrow-btn arrow-next"><svg width="14" height="14" viewBox="0 0 24 24"><path d="M9 5l7 7-7 7" stroke="#fff" stroke-width="3" fill="none"/></svg></div>
<div class="abs testi-photo" role="img" aria-label="Photo of the reviewing customers"></div>
<div class="abs testi-badge"></div>
<p class="abs testi-quote">"They did an excellent job. It great! It only took on day, and the installers did and excellent job cleaning up...I highly recommend them if you went a professional job done right"</p>
<div class="abs testi-meta">
  <span>CUSTOMER NAME</span><span class="sep">|</span><span>VERIFIED REVIEW</span><span class="sep">|</span><span class="stars">★★★★★</span>
</div>

<!-- call to action -->
<div class="abs cta-photo" role="img" aria-label="Photo of a house garden with a curved path through a lawn"></div>
<div class="abs cta-shade"></div>
<h2 class="abs cta-title">We take care of your landscape.<br>You take back your free time.</h2>
<a class="abs cta-btn">Start my estimate
  <svg width="16" height="16" viewBox="0 0 24 24"><circle cx="12" cy="12" r="11" fill="#fff"/><path d="M10 7l5 5-5 5" stroke="var(--green)" stroke-width="2.5" fill="none"/></svg>
</a>

<!-- footer -->
<svg class="abs footer-shape" width="1200" height="482" viewBox="0 0 1200 482">
  <polygon points="0,120 600,12 1200,120 1200,482 0,482" fill="var(--green)"/>
  <polygon points="0,134 600,26 1200,134 1200,482 0,482" fill="var(--footer)"/>
</svg>

<div class="abs estimate-card">
  <h3>Get a free estimate</h3>
  <p>Fill out the form below and a representative will be in touch.</p>
  <div class="field" style="left:16px;top:87px;width:126px">Name</div>
  <div class="field" style="left:153px;top:87px;width:125px">Phone</div>
  <div class="field" style="left:16px;top:121px;width:126px">Email</div>
  <div class="field" style="left:153px;top:121px;width:125px">Address</div>
  <div class="field" style="left:16px;top:155px;width:262px">Estimate type
    <span class="field-select-btn"><svg width="8" height="6" viewBox="0 0 8 6"><path d="M0 0h8L4 6z" fill="#fff"/></svg></span>
  </div>
  <div class="field" style="left:16px;top:189px;width:262px;height:69px">How can we help ?</div>
  <div class="card-btn">Start my estimate
    <svg width="10" height="10" viewBox="0 0 24 24"><circle cx="12" cy="12" r="11" fill="#fff"/><path d="M10 7l5 5-5 5" stroke="var(--green)" stroke-width="3" fill="none"/></svg>
  </div>
</div>

<div class="abs footer-brand">
  <span class="brand-square"></span>
  <span class="brand-name">Verdant<br>Ridge</span>
</div>

<div class="abs fcol" style="left:384px;top:4341px;width:110px;height:130px">
  <a class="flink" style="top:0">Home</a>
  <a class="flink" style="top:36px">About Us</a>
  <a class="flink" style="top:72px">Projects</a>
  <a class="flink" style="top:106px">Contact</a>
</div>
<div class="abs fcol" style="left:504px;top:4339px;width:110px;height:130px">
  <span class="flink" style="top:0">Services</span>
  <a class="flink fsub" style="top:36px">Building</a>
  <a class="flink fsub" style="top:64px">Landscaping</a>
  <a class="flink fsub" style="top:91px">Decking</a>
</div>
<div class="abs fcol" style="left:633px;top:4339px;width:110px;height:130px">
  <span class="flink" style="top:0">Services</span>
  <a class="flink fsub" style="top:36px">Maintenance</a>
  <a class="flink fsub" style="top:64px">Roofing</a>
  <a class="flink fsub" style="top:91px">Gutters</a>
</div>

<div class="abs social" aria-label="Social links">
  <span></span><span></span><span></span><span></span>
</div>
<div class="abs footer-rule"></div>
<p class="abs copyright">© 2024 Verdant Ridge. All Rights are Reserved.</p>

</body>
</html>
```